Powerpoint template & style design project

KLavender Consulting is an IT technology firm specializing in mobility and telecommunications applications. We provide technical consulting to global companies that want to build mobile applications and take critical business applications and move them into the cloud.
We would like to see designs that use the color blue. The final design should communicate confidence, agility and speak to technology focused customers. Forward progress and/or motion should be conveyed.

Target Market(s)

Government customers and large enterprise companies

Industry/Entity Type

Telecommunications

Font styles to use
Sans Serif

Colors
0555a3

Requirements
Must have
• different slides: Cover page, title slide, main content, transition slide, close out slide..

```html
<!DOCTYPE html>
<html lang="en">
<head>
<meta charset="utf-8">
<title>KLavender Consulting – Presentation Template</title>
<link rel="stylesheet" href="https://fonts.googleapis.com/css2?family=Arimo:wght@400;700&family=Montserrat:wght@500;700&display=swap">
<style>
  :root {
    --brand-blue: #0555a3;
    --brand-blue-soft: #5c8fc6;
    --stage-black: #000000;
    --paper: #ffffff;
    --ink: #000000;
    --tag-grey: #4a4a4a;
  }
  * { margin: 0; padding: 0; box-sizing: border-box; }
  html, body {
    width: 1200px; height: 1000px; overflow: hidden;
    background: var(--stage-black);
  }
  .board { position: relative; width: 1200px; height: 1000px; }
  .slide {
    position: absolute; width: 549px; height: 456px;
    background: var(--paper); overflow: hidden;
  }
  .slide--cover { left: 20px; top: 20px; }
  .slide--content { left: 632px; top: 20px; width: 548px; }
  .slide--transition { left: 20px; top: 524px; background: var(--brand-blue); }
  .slide--closing { left: 632px; top: 524px; width: 548px; }

  .footer-band {
    position: absolute; left: 0; right: 0; bottom: 0; height: 124px;
    background: linear-gradient(to bottom, var(--brand-blue-soft) 0%, var(--brand-blue) 45%, var(--brand-blue) 100%);
  }

  .cover-title {
    position: absolute; left: 0; right: 0; top: 134px;
    text-align: center;
    font-family: "Arimo", Arial, sans-serif; font-weight: 700;
    font-size: 32px; line-height: 41px; letter-spacing: 1.2px; color: var(--ink);
  }
  .content-text {
    position: absolute; left: 30px; top: 157px; right: 8px;
    font-family: "Arimo", Arial, sans-serif; font-weight: 700;
    font-size: 19px; line-height: 23px; letter-spacing: 0.6px; color: var(--ink);
  }

  .mini-brand {
    position: absolute; right: 28px; bottom: 12px;
    text-align: center; color: var(--paper);
    font-family: "Montserrat", Arial, sans-serif;
  }
  .mini-brand__name { font-weight: 700; font-size: 12px; letter-spacing: -0.3px; line-height: 14px; }
  .mini-brand__tag { font-weight: 500; font-size: 5px; letter-spacing: 0.8px; }

  .brand {
    position: absolute; left: 0; right: 0; top: 236px;
    text-align: center; font-family: "Montserrat", Arial, sans-serif;
  }
  .brand__name {
    font-weight: 700; font-size: 34px; letter-spacing: -1.2px; line-height: 44px;
  }
  .brand__tag {
    margin-top: -3px; font-weight: 500; font-size: 13px; letter-spacing: 2.8px;
  }
  .slide--transition .brand__name,
  .slide--transition .brand__tag { color: var(--paper); }
  .slide--closing .brand__name { color: var(--brand-blue); }
  .slide--closing .brand__tag { color: var(--tag-grey); }
</style>
</head>
<body>
<main class="board">

  <section class="slide slide--cover">
    <h1 class="cover-title">KLavender Consulting<br>Welcome to presentation<br>April 2015</h1>
    <div class="footer-band" role="img" aria-label="Blue flowing wave band along the bottom of the slide"></div>
    <div class="mini-brand">
      <div class="mini-brand__name">KLavender Consulting</div>
      <div class="mini-brand__tag">MOBILITY &amp; TELECOMMUNICATIONS</div>
    </div>
  </section>

  <section class="slide slide--content">
    <p class="content-text">we specialize in:Mobility and Telecommunications:<br>Strategy, Planning &amp; ManagementPeople,<br>Process and Technology Solutions</p>
    <div class="footer-band" role="img" aria-label="Blue flowing wave band along the bottom of the slide"></div>
    <div class="mini-brand">
      <div class="mini-brand__name">KLavender Consulting</div>
      <div class="mini-brand__tag">MOBILITY &amp; TELECOMMUNICATIONS</div>
    </div>
  </section>

  <section class="slide slide--transition">
    <div class="brand">
      <div class="brand__name">KLavender Consulting</div>
      <div class="brand__tag">MOBILITY &amp; TELECOMMUNICATIONS</div>
    </div>
  </section>

  <section class="slide slide--closing">
    <div class="brand">
      <div class="brand__name">KLavender Consulting</div>
      <div class="brand__tag">MOBILITY &amp; TELECOMMUNICATIONS</div>
    </div>
  </section>

</main>
</body>
</html>
```